Review Site Redesign

We have a rather ambitious goal to reinvent (redesign) the way bank financial review sites present information. In that respect, we’re looking for an innovative creative design.
As examples of what I would call bad or boring design please look at the following sites:
1. http://brindlelend.example/se
2. http://corvalmoney.example/se/privatlan
3. http://fjellpurse.example/no
These are the traditional way these types of review sites are organized: dull and boring. I think we can do a lot better than that.
I need a site that will capture attention end engage the visitor; a site that will create a more interactive and less passive user experience.
Scope of work should also include logo font and additional content space for articles, FAQ, widgets, social media links, etc.

Not sure what to advise you as best format - maybe a flash or js carousel, gallery, wheel, logo image matrix, or something else.
Maybe some kind of interactive logo matrix such as this site: http://www.lumvikra.example/
Please apply your best creative mind work to this problem.
Also, please think about creative use of background images, stock photos, etc.
For logo font use can use URL “quillfunds.example” as placeholder.

Industry/Entity Type

Bank

```html
<!DOCTYPE html>
<html lang="no">
<head>
<meta charset="utf-8">
<title>Quill Funds</title>
<link href="https://fonts.googleapis.com/css2?family=Oswald:wght@400&family=PT+Sans+Narrow:wght@400;700&family=Arimo&display=swap" rel="stylesheet">
<style>
:root{
  --yellow:#f6b800;
  --yellow-dark:#e3a300;
  --ink:#2a2a2a;
  --text:#555;
  --muted:#777;
  --panel:#fff;
  --widget:#dcdcdc;
  --footer-dark:#2b2b2b;
}
*{margin:0;padding:0;box-sizing:border-box}
html,body{width:667px;height:1200px;overflow:hidden}
body{position:relative;font-family:"PT Sans Narrow",Arial,sans-serif;color:var(--text);
  background:linear-gradient(90deg,#6a6a6a 0%,#bdbdbd 12%,#8a8a8a 22%,#d4d4d4 35%,#9c9c9c 48%,#e0e0e0 60%,#8f8f8f 72%,#c9c9c9 85%,#6e6e6e 100%);}
.abs{position:absolute}
.brand{left:46px;top:6px;display:flex;flex-direction:column;align-items:flex-start}
.brand-dot{width:62px;height:62px;border-radius:50%;background:var(--yellow);margin-left:22px}
.brand-name{font-family:"PT Sans Narrow",sans-serif;font-size:13px;color:#555;margin-top:2px;margin-left:12px}
.main-nav{left:55px;top:85px;width:556px;height:27px;background:linear-gradient(#ffc928,var(--yellow-dark));display:flex}
.main-nav a{font-family:"Oswald",sans-serif;font-size:10px;color:var(--ink);text-decoration:none;height:27px;line-height:27px;text-align:center;border-right:1px solid #d69800}
.hero{left:55px;top:112px;width:556px;height:236px;background:linear-gradient(120deg,#cfd6dc 0%,#8e9aa5 35%,#5a4a40 55%,#b7c2cc 80%,#e6ecef 100%)}
.hero-caption{left:7px;top:81px;width:210px;padding:7px 8px;background:rgba(40,40,40,.78);color:#fff;font-family:"Oswald",sans-serif;font-size:8.6px;line-height:13px;text-transform:uppercase}
.hero-dots{right:20px;bottom:7px;display:flex;gap:3px}
.hero-dots span{width:6px;height:6px;border-radius:50%;background:var(--yellow)}
.hero-dots span:first-child{background:#333}
.tagline{left:55px;top:348px;width:556px;height:27px;background:var(--yellow);font-family:"Oswald",sans-serif;font-size:13px;letter-spacing:-0.15px;line-height:27px;color:var(--ink);padding-left:8px;white-space:nowrap;overflow:hidden}
.panel{background:var(--panel);border:1px solid #d0d0d0;border-radius:5px}
.info{left:57px;top:388px;width:554px;height:229px}
.info-col{top:12px;width:163px}
.info-col h2{font-family:"Oswald",sans-serif;font-weight:400;font-size:14px;color:var(--ink);height:22px}
.info-photo{width:163px;height:83px;border:1px solid #8aa;border-radius:4px;background:linear-gradient(120deg,#cfd3d6,#7e8790 45%,#c0b6aa 70%,#e9ecee)}
.info-col p{font-family:"Arimo",Arial,sans-serif;font-size:7.4px;line-height:11.3px;color:var(--muted);margin-top:7px;text-align:justify}
.content{left:57px;top:627px;width:554px;height:472px}
.ribbon{height:20px;background:var(--yellow);color:#fff;font-family:"Oswald",sans-serif;font-size:11px;line-height:20px;padding-left:13px}
.ribbon svg{position:absolute;left:0;top:20px}
.post{left:62px;width:252px}
.post.divided{border-bottom:1px dashed #aaa}
.post h3{font-weight:400;font-size:10.5px;line-height:13px;color:var(--ink);margin-bottom:2px}
.post p{font-size:6.9px;line-height:12px;color:var(--ink);text-align:justify}
.post .meta{font-size:6.9px;color:var(--muted);margin-top:4px;text-align:left}
.widget{left:368px;width:238px;background:var(--widget);text-align:center}
.widget h4{font-family:"Oswald",sans-serif;font-weight:400;font-size:17px;color:var(--yellow);margin-top:8px}
.site-footer{left:55px;top:1108px;width:556px;height:50px;background:var(--yellow);border-radius:4px}
.foot-nav a{position:absolute;top:21px;font-family:"Oswald",sans-serif;font-size:7px;color:var(--ink);text-decoration:none}
.follow{left:356px;top:9px;width:200px;height:31px;background:var(--footer-dark);border-radius:6px 0 0 6px;color:#bbb;font-family:"Oswald",sans-serif;font-size:7px;line-height:31px;padding-left:14px}
.copyright{left:0;top:1166px;width:667px;text-align:center;font-family:"Oswald",sans-serif;font-size:6.5px;color:#fff}
</style>
</head>
<body>

<div class="abs brand"><span class="brand-dot"></span><span class="brand-name">Quill Funds</span></div>

<nav class="abs main-nav">
  <a style="width:108px" href="#">HEM</a>
  <a style="width:86px" href="#">ALLT OM EKONOMI</a>
  <a style="width:106px" href="#">EKONOMI ORDBOK</a>
  <a style="width:72px" href="#">OM OSS</a>
  <a style="width:76px" href="#">KONTAKT</a>
  <a style="width:108px;border-right:none" href="#">FORUM</a>
</nav>

<section class="abs hero" role="img" aria-label="Foto av ett smilende par foran en bærbar datamaskin">
  <p class="abs hero-caption">Fjellpurse sammenligner og vurderer online lån. Formålet er, å gi deg som bruker muligheten for å finne et lån, som passer til nettopp dine behov.</p>
  <div class="abs hero-dots"><span></span><span></span><span></span><span></span><span></span></div>
</section>

<div class="abs tagline">SÅ LÅNAR DU PENGAR DIREKT&nbsp; : Ibland kan man hamna i en situation där man behöver låna pengar direkt.</div>

<section class="abs panel info">
  <article class="abs info-col" style="left:15px">
    <h2>BANK LOAN INFO 1</h2>
    <div class="info-photo" role="img" aria-label="Foto av hender som overleverer et kort over et skrivebord"></div>
    <p>Lorem ipsum dolor sit amet, consectetuer adipiscing elit, sed diam nonummy nibh euismod tincidunt ut laoreet dolore magna aliquam erat volutpat. Ut wisi enim. Lorem ipsum dolor sit amet, consectetuer adipiscing elit, sed diam nonummy nibh euismod tincidunt ut laoreet dolore magna aliquam erat volutpat. Ut wisi enim.</p>
  </article>
  <article class="abs info-col" style="left:198px">
    <h2>BANK LOAN INFO 1</h2>
    <div class="info-photo" role="img" aria-label="Foto av hender som overleverer et kort over et skrivebord"></div>
    <p>Lorem ipsum dolor sit amet, consectetuer adipiscing elit, sed diam nonummy nibh euismod tincidunt ut laoreet dolore magna aliquam erat volutpat. Ut wisi enim. Lorem ipsum dolor sit amet, consectetuer adipiscing elit, sed diam nonummy nibh euismod tincidunt ut laoreet dolore magna aliquam erat volutpat. Ut wisi enim.</p>
  </article>
  <article class="abs info-col" style="left:376px">
    <h2>BANK LOAN INFO 1</h2>
    <div class="info-photo" role="img" aria-label="Foto av hender som overleverer et kort over et skrivebord"></div>
    <p>Lorem ipsum dolor sit amet, consectetuer adipiscing elit, sed diam nonummy nibh euismod tincidunt ut laoreet dolore magna aliquam erat volutpat. Ut wisi enim. Lorem ipsum dolor sit amet, consectetuer adipiscing elit, sed diam nonummy nibh euismod tincidunt ut laoreet dolore magna aliquam erat volutpat. Ut wisi enim.</p>
  </article>
</section>

<section class="abs panel content"></section>

<div class="abs ribbon" style="left:47px;top:636px;width:115px">LATEST ARTICLES
  <svg width="8" height="8"><polygon points="0,0 8,0 8,8" fill="#b57f00"/></svg>
</div>
<svg class="abs" style="left:150px;top:636px" width="13" height="20"><polygon points="0,0 13,10 0,20" fill="#f6b800"/></svg>

<article class="abs post divided" style="top:662px;height:90px">
  <h3>Slik låner du penger</h3>
  <p>Det er ekstremt lett å låne penger bare for å gjøre hverdagen litt søtere. Det kan gjøres i løpet av 5 minutter på hjemmesiden til låneutbyderne. Du trenger bare å fylle inn dine private opplysninger og kontoopplysninger, velge lånebeløp og hvordan du vil dele opp avdragene. Når der er gjort, kan du slappe av og lene deg tilbake mens du venter på at din søknad om å låne penger blir vurdert.</p>
  <p class="meta">Author: admin &nbsp;&nbsp;|&nbsp;&nbsp; Posted in Slik låner du penger</p>
</article>
<article class="abs post divided" style="top:759px;height:88px">
  <h3>Slik låner du penger</h3>
  <p>Det er ekstremt lett å låne penger bare for å gjøre hverdagen litt søtere. Det kan gjøres i løpet av 5 minutter på hjemmesiden til låneutbyderne. Du trenger bare å fylle inn dine private opplysninger og kontoopplysninger, velge lånebeløp og hvordan du vil dele opp avdragene. Når der er gjort, kan du slappe av og lene deg tilbake mens du venter på at din søknad om å låne penger blir vurdert.</p>
  <p class="meta">Author: admin &nbsp;&nbsp;|&nbsp;&nbsp; Posted in Slik låner du penger</p>
</article>
<article class="abs post" style="top:852px">
  <h3>Slik låner du penger</h3>
  <p>Det er ekstremt lett å låne penger bare for å gjøre hverdagen litt søtere. Det kan gjøres i løpet av 5 minutter på hjemmesiden til låneutbyderne. Du trenger bare å fylle inn dine private opplysninger og kontoopplysninger, velge lånebeløp og hvordan du vil dele opp avdragene. Når der er gjort, kan du slappe av og lene deg tilbake mens du venter på at din søknad om å låne penger blir vurdert.</p>
  <p class="meta">Author: admin &nbsp;&nbsp;|&nbsp;&nbsp; Posted in Slik låner du penger</p>
</article>

<div class="abs ribbon" style="left:47px;top:947px;width:104px">FAQ
  <svg width="8" height="8"><polygon points="0,0 8,0 8,8" fill="#b57f00"/></svg>
</div>
<svg class="abs" style="left:150px;top:947px" width="13" height="20"><polygon points="0,0 13,10 0,20" fill="#f6b800"/></svg>

<article class="abs post divided" style="top:973px;height:56px">
  <h3>Søk online hos en godkjent utbyder ?</h3>
  <p>Du kan søke om lån hos utbyderne over. Alle er godkjente til å drive med lånevirksomhet i Norge, så du kan være sikker på at du får et lån med ordentlige og rettferdige vilkår. Klikk på linken og søk online på utbydernes hjemmesider.</p>
</article>
<article class="abs post" style="top:1031px">
  <h3>Søk online hos en godkjent utbyder ?</h3>
  <p>Du kan søke om lån hos utbyderne over. Alle er godkjente til å drive med lånevirksomhet i Norge, så du kan være sikker på at du får et lån med ordentlige og rettferdige vilkår. Klikk på linken og søk online på utbydernes hjemmesider.</p>
</article>

<aside class="abs widget" style="top:634px;height:213px"><h4>WIDGETS</h4></aside>
<aside class="abs widget" style="top:868px;height:214px"><h4>WIDGETS</h4></aside>

<footer class="abs site-footer">
  <nav class="foot-nav">
    <a style="left:11px" href="#">HEM</a>
    <a style="left:55px" href="#">ALLT OM EKONOMI</a>
    <a style="left:133px" href="#">EKONOMI ORDBOK</a>
    <a style="left:211px" href="#">OM OSS</a>
    <a style="left:262px" href="#">KONTAKT</a>
    <a style="left:319px" href="#">FORUM</a>
  </nav>
  <div class="abs follow">FOLLOW US ON :
    <svg class="abs" style="left:68px;top:5px" width="110" height="21">
      <circle cx="10.5" cy="10.5" r="9" fill="none" stroke="#777" stroke-width="1.5"/>
      <circle cx="36" cy="10.5" r="9" fill="none" stroke="#777" stroke-width="1.5"/>
      <circle cx="61" cy="10.5" r="9" fill="none" stroke="#777" stroke-width="1.5"/>
      <circle cx="88" cy="10.5" r="9" fill="none" stroke="#777" stroke-width="1.5"/>
    </svg>
  </div>
</footer>

<p class="abs copyright">COPYRIGHT © QUILL FUNDS&nbsp; 2012&nbsp; - ALL RIGHTS RESERVED</p>

</body>
</html>
```